Silverwell Tisane House needs a website with shopping cart

We are a herbal tea business that hand blends organic tea recipes for medicinal purposes and for customer enjoyment. We require a website that represents our elegant brand and our connection to plant medicine. We will require a home page, a products page, a contact us page with form and an information page. We will need to be able to photograph our teas and upload the images to the products page along with changing pricing and shipping costs, and the ability to add/change information and images to our information page as this page will be mostly about the different herbs we will use in the teas. Our teas will be 'loose leaf' (not in tea bags) and will be sold in glass jars. At this stage we only intend to use Quorvex as a method of payment for overseas customers and direct credit for New Zealand customers.

Target Market(s)

Tea drinkers, women, people interested in health/herbs, people looking for gifts

Industry/Entity Type

Shopping

Logo Text

Silverwell Tisane House

Coding

Coded - Design and coding required

Number of Pages Required

4 page

Font styles to use
Decorative

Requirements
Must have
• I am a herbalist and love plants, flowers and nature so would like the overall website and logo to represent this. I have attached the logo I had designed several years ago for myself as inspiration - the graduated greens are great and very vibrant which I like (sorry about the quality, I couldn't find the source files - NEW SOURCE FILE ADDED 23/04/15). This is an upmarket, niche product which is elegant and healthy.

```html
<!DOCTYPE html>
<html lang="en">
<head>
<meta charset="utf-8">
<title>Silverwell Tisane House – Home</title>
<link href="https://fonts.googleapis.com/css2?family=Cagliostro&family=PT+Sans:wght@400;700&display=swap" rel="stylesheet">
<style>
:root{
  --green:#7ab840;
  --green-dark:#4f8a1c;
  --green-light:#b9dc6a;
  --yellow:#f2c81a;
  --orange:#dfa11e;
  --ink:#333;
  --charcoal:#27292c;
  --footer:#2b2d30;
  --white:#fff;
  --frame:#000;
}
*{box-sizing:border-box;margin:0;padding:0}
html,body{width:900px;height:1200px;overflow:hidden;background:var(--frame)}
body{position:relative;font-family:"Cagliostro",sans-serif;color:var(--ink)}
.page{position:absolute;left:68px;top:2px;width:768px;height:1198px;background:var(--white);overflow:hidden}
.abs{position:absolute}
.btn{position:absolute;display:flex;align-items:center;justify-content:center;gap:4px;font-family:"PT Sans",sans-serif;font-size:9px;color:var(--white);background:var(--green)}
.btn svg{width:10px;height:10px}

/* header */
.site-header{left:0;top:0;width:768px;height:60px;background:var(--white);border-bottom:2px solid var(--green)}
.brand{left:162px;top:6px;width:96px;text-align:center}
.brand-mark{width:26px;height:26px;border-radius:50%;background:var(--green);margin:0 auto 3px}
.brand-name{font-size:9px;letter-spacing:.5px;color:var(--green-dark);text-transform:uppercase}
.brand-tag{font-family:"PT Sans",sans-serif;font-size:4px;color:var(--green);margin-top:1px}
.icon-dot{top:8px;width:14px;height:14px;border-radius:50%;background:var(--green);display:flex;align-items:center;justify-content:center}
.icon-dot svg{width:8px;height:8px}
.btn-login{left:507px;top:7px;width:44px;height:17px;border-radius:2px;font-size:7px}
.btn-signup{left:556px;top:7px;width:44px;height:17px;border-radius:2px;font-size:7px;background:var(--yellow)}
.main-nav{top:33px;left:362px;display:flex;gap:0;font-size:10.5px}
.main-nav a{color:#222;text-decoration:none;position:absolute;white-space:nowrap}
.main-nav .current{color:var(--green)}
.nav-leaf{left:351px;top:45px}

/* hero */
.hero{left:0;top:60px;width:768px;height:340px;background:radial-gradient(ellipse at 20% 30%,#c9e36a 0%,#8fc23a 45%,#5e9a1c 100%)}
.hero-panel{left:150px;top:0;width:468px;height:220px;background:linear-gradient(135deg,#b8d85a 0%,#9cc83f 55%,#79ad2a 100%)}
.hero-photo{left:200px;top:80px;width:262px;height:140px;border-radius:50% 50% 0 0/40% 40% 0 0;background:radial-gradient(ellipse at 55% 60%,#f3d27a 0%,#d7a73a 35%,rgba(150,180,60,0) 75%)}
.hero-kicker{left:194px;top:10px;font-size:28px;color:var(--yellow)}
.hero-title{left:194px;top:42px;font-size:21px;color:var(--white)}
.hero-lede{left:196px;top:86px;width:230px;font-family:"PT Sans",sans-serif;font-size:10.5px;line-height:14px;color:var(--white)}
.btn-outline{left:196px;top:140px;width:80px;height:20px;background:none;border:1px solid var(--white);font-family:"Cagliostro",sans-serif;font-size:10px;color:var(--yellow)}
.promo{top:232px;height:108px;display:flex;flex-direction:column;align-items:center;justify-content:center;text-align:center}
.promo-new{left:156px;width:224px;background:linear-gradient(120deg,#6f5a3a,#c8a15a 50%,#4a3a28)}
.promo-sample{left:388px;width:224px;background:linear-gradient(120deg,#3a2a1c,#7a5a3a 55%,#2c2218)}
.promo-line{font-size:22px;line-height:26px;color:var(--white)}
.promo-line.accent{color:var(--yellow)}
.promo-sub{font-family:"PT Sans",sans-serif;font-size:10px;color:var(--yellow);font-weight:700}
.promo .btn{position:static;margin-top:6px;height:16px;padding:0 6px;background:var(--yellow);color:var(--ink)}
.promo .btn .cart-box{background:var(--green);width:16px;height:16px;margin-left:-6px;display:flex;align-items:center;justify-content:center}

/* welcome */
.welcome-band{left:0;top:400px;width:768px;height:36px;background:var(--green);border-bottom:3px solid var(--green-dark);color:var(--white);font-size:17px;display:flex;align-items:center;justify-content:center}
.leaf-art{left:156px;top:440px;width:72px;height:80px;background:radial-gradient(ellipse at 50% 50%,#8cc63f 0%,#5e9a1c 45%,rgba(255,255,255,0) 72%)}
.welcome-copy{left:231px;top:444px;width:144px;font-family:"PT Sans",sans-serif;font-size:8px;line-height:14.5px;color:#444}
.btn-view{width:52px;height:15px;font-size:8px}
.craft-title{left:445px;top:438px;font-size:13px;color:#333}
.craft-photo{left:418px;width:48px;height:46px;border-radius:2px}
.craft-name{left:505px;font-size:10.5px;color:var(--green)}
.craft-note{left:505px;width:106px;font-family:"PT Sans",sans-serif;font-size:4.5px;line-height:6px;color:#555}
.rule{left:156px;width:456px;height:1px;background:#e4e4e4}

/* products */
.tab{top:642px;height:40px;font-size:14px;display:flex;align-items:center}
.tab.active{left:163px;width:80px;background:var(--green);color:var(--white);justify-content:center}
.product-frame{top:698px;width:92px;height:92px;background:#fffdf6;border:3px solid #f4ecd8;box-shadow:0 2px 3px rgba(0,0,0,.12);display:flex;align-items:center;justify-content:center}
.product-photo{width:72px;height:72px;border-radius:50%}
.product-name{top:794px;width:100px;font-size:9.5px;line-height:12px;color:var(--orange)}
.product-price{font-family:"PT Sans",sans-serif;font-size:6.5px;color:#444}
.stars{font-size:6px;color:var(--orange);font-family:"PT Sans",sans-serif}

/* banner */
.offer{left:0;top:884px;width:768px;height:136px;background:radial-gradient(ellipse at 50% 40%,#d9ec9a 0%,#9bc843 50%,#5e9a1c 100%)}
.offer-panel{left:150px;top:0;width:468px;height:136px;background:linear-gradient(180deg,#b9d98a 0%,#7fb33a 100%)}
.offer-title{left:150px;top:0;width:468px;text-align:center;font-size:27px;line-height:37px;color:var(--white)}
.btn-shop{left:346px;top:110px;height:17px;padding-right:6px;background:var(--charcoal)}
.btn-shop .cart-box{background:var(--green);width:17px;height:17px;display:flex;align-items:center;justify-content:center}

/* newsletter */
.newsletter{left:0;top:1020px;width:768px;height:40px;background:var(--charcoal);color:var(--white)}
.newsletter-text{left:166px;top:7px;font-family:"PT Sans",sans-serif;font-size:17px}
.btn-subscribe{left:522px;top:9px;width:61px;height:22px;font-size:10px}

/* footer */
.field-left,.field-right{top:1060px;width:150px;height:140px;background:linear-gradient(180deg,#d4e86a 0%,#8cc23a 40%,#3f7a14 100%)}
.field-left{left:0}.field-right{left:618px}
.site-footer{left:150px;top:1060px;width:468px;height:140px;background:var(--footer);color:#e8e8e8;font-family:"PT Sans",sans-serif}
.footer-col{position:absolute;top:6px}
.footer-col h4{font-size:8.5px;font-weight:400;text-transform:uppercase;margin-bottom:14px;color:var(--white)}
.footer-col ul{list-style:none;font-size:8px;line-height:10.6px}
.blog-photo{width:74px;height:52px;background:linear-gradient(160deg,#eee,#8a8a8a);margin:0 0 4px -4px}
.blog-text{font-size:6px;line-height:8px;width:88px;color:#ccc}
.blog-text span{color:var(--orange)}
.social{display:flex;gap:8px;margin-top:6px}
.social span{font-size:7px;color:var(--green)}
.contact-line{display:flex;gap:6px;font-size:6.5px;line-height:8.5px;margin-top:4px}
.contact-line svg{flex:none;width:8px;height:8px;margin-top:1px}
</style>
</head>
<body>
<div class="page">

  <header class="site-header abs">
    <div class="brand abs">
      <div class="brand-mark"></div>
      <div class="brand-name">Maren Holloway</div>
      <div class="brand-tag">NATUROPATH, HERBALIST &amp; NUTRITIONIST</div>
    </div>
    <div class="icon-dot abs" style="left:462px">
      <svg viewBox="0 0 10 10"><circle cx="4" cy="4" r="2.8" fill="none" stroke="#fff" stroke-width="1.4"/><line x1="6" y1="6" x2="9" y2="9" stroke="#fff" stroke-width="1.4"/></svg>
    </div>
    <div class="icon-dot abs" style="left:481px">
      <svg viewBox="0 0 10 10"><path d="M1 2h1.5l1.2 4.5h4.3L9 3H3" fill="none" stroke="#fff" stroke-width="1.1"/><circle cx="4" cy="8.3" r=".9" fill="#fff"/><circle cx="7.4" cy="8.3" r=".9" fill="#fff"/></svg>
    </div>
    <a class="btn btn-login">LOG IN</a>
    <a class="btn btn-signup">SIGN UP</a>
    <nav class="main-nav abs" style="left:0">
      <a class="current" style="left:361px">Home</a>
      <a style="left:413px">Our products</a>
      <a style="left:484px">Information</a>
      <a style="left:556px">Contact us</a>
    </nav>
    <svg class="nav-leaf abs" width="32" height="12" viewBox="0 0 32 12"><path d="M1 10 Q14 -2 31 3 Q18 12 1 10Z" fill="var(--green)"/></svg>
  </header>

  <section class="hero abs" role="img" aria-label="Blurred close-up of fresh green tea leaves in sunlight">
    <div class="hero-panel abs"></div>
    <div class="hero-photo abs" role="img" aria-label="Glass teapot and cup of golden herbal tea with dried flowers"></div>
    <div class="hero-kicker abs">World's</div>
    <h1 class="hero-title abs" style="font-weight:400">Best Herbal Brew Collection</h1>
    <p class="hero-lede abs">For us is a very simple call to action that we trust will lead you to improved health and well-being.</p>
    <a class="btn btn-outline">Read more</a>

    <div class="promo promo-new abs" role="img" aria-label="Cup of herbal tea with fruit and berries">
      <div class="promo-line accent">NEW</div>
      <div class="promo-line">ARRIVALS</div>
      <a class="btn"><span class="cart-box"><svg viewBox="0 0 10 10"><path d="M1 2h1.5l1.2 4.5h4.3L9 3H3" fill="none" stroke="#fff" stroke-width="1.1"/><circle cx="4" cy="8.3" r=".9" fill="#fff"/><circle cx="7.4" cy="8.3" r=".9" fill="#fff"/></svg></span>ENTER NOW</a>
    </div>
    <div class="promo promo-sample abs" role="img" aria-label="Loose leaf tea samples on a wooden table">
      <div class="promo-line">FREE SAMPLE</div>
      <div class="promo-sub">WITH EVERY ONLINE ORDER</div>
      <a class="btn"><span class="cart-box"><svg viewBox="0 0 10 10"><path d="M1 2h1.5l1.2 4.5h4.3L9 3H3" fill="none" stroke="#fff" stroke-width="1.1"/><circle cx="4" cy="8.3" r=".9" fill="#fff"/><circle cx="7.4" cy="8.3" r=".9" fill="#fff"/></svg></span>SHOP NOW</a>
    </div>
  </section>

  <h2 class="welcome-band abs" style="font-weight:400">Welcome to our site !</h2>

  <div class="leaf-art abs" role="img" aria-label="Sprig of fresh green tea leaves"></div>
  <p class="welcome-copy abs">Welcome to Silverwell Tisane House, the site of herbal-craft tea blending. We offer a selection of herbal teas that have been blended for exquisite flavour, aroma and interest, and those that are helpful in assisting with common ailments and conditions. Our herbs are organically sourced both locally and internationally with excellence in quality being of utmost importance.</p>
  <a class="btn btn-view" style="left:231px;top:593px">View all</a>

  <h3 class="craft-title abs" style="font-weight:400">The Craft of Brewing</h3>
  <div class="craft-photo abs" style="top:460px;background:radial-gradient(circle,#e0902a 0%,#f6f0e4 60%)" role="img" aria-label="Cup of hot amber herbal infusion"></div>
  <div class="craft-name abs" style="top:464px">Hot Infusions</div>
  <p class="craft-note abs" style="top:484px">Infusions are the usual way we brew tea where herbs are left to steep in boiled water for 3-5 minutes.</p>
  <div class="craft-photo abs" style="top:512px;background:radial-gradient(circle,#5a1820 0%,#2a2a2e 55%,#ddd 80%)" role="img" aria-label="Bowl of dark red cold infusion"></div>
  <div class="craft-name abs" style="top:515px">Cold Infusions</div>
  <p class="craft-note abs" style="top:535px">Cold infusions are where the herbs are left covered, in cold water, overnight to allow the constituents to be released.</p>
  <div class="craft-photo abs" style="top:566px;background:radial-gradient(circle,#9ccc3a 0%,#cfe7a0 50%,#fff 78%)" role="img" aria-label="Glass teapot with green herbs steeping"></div>
  <div class="craft-name abs" style="top:566px">Decoctions</div>
  <p class="craft-note abs" style="top:586px">With decoctions, herbs are either placed in a pot with cold water and brought to the boil, or added to a pot with boiling water for 15-20 minutes.</p>

  <div class="rule abs" style="top:632px"></div>

  <div class="tab active abs">Popular</div>
  <div class="tab abs" style="left:259px;color:var(--green);top:644px">New arrivals</div>
  <div class="tab abs" style="left:366px;color:var(--green);top:642px">Best sellers</div>

  <div class="product-frame abs" style="left:163px"><div class="product-photo" style="background:radial-gradient(circle,#e8c050,#b8862a)" role="img" aria-label="Pile of dried chamomile flowers"></div></div>
  <div class="product-frame abs" style="left:279px"><div class="product-photo" style="background:radial-gradient(circle,#c89a5a,#8a5a2a)" role="img" aria-label="Cinnamon apple chamomile loose leaf blend"></div></div>
  <div class="product-frame abs" style="left:395px"><div class="product-photo" style="background:radial-gradient(circle,#6a7a4a,#3a4a2c)" role="img" aria-label="Green tea blend with blue petals"></div></div>
  <div class="product-frame abs" style="left:511px"><div class="product-photo" style="background:radial-gradient(circle,#c8985a,#8a5a30)" role="img" aria-label="Pile of dried ginger root pieces"></div></div>

  <div class="product-name abs" style="left:163px">Chamomile<div class="product-price">Starting at:NZ$2.00</div></div>
  <div class="product-name abs" style="left:279px">Cinnamon apple<br>chamomile<div class="stars">★★★★½ 9</div><div class="stars">Review (s)</div><div class="product-price" style="margin-top:6px">Starting at:NZ$2.00</div></div>
  <div class="product-name abs" style="left:395px">Fountain of youth<div class="product-price">Starting at:NZ$2.00</div></div>
  <div class="product-name abs" style="left:511px">Ginger root<div class="product-price">Starting at:NZ$2.00</div></div>
  <a class="btn btn-view" style="left:552px;top:841px;font-size:9px">View all</a>

  <div class="rule abs" style="top:870px"></div>

  <section class="offer abs" role="img" aria-label="Iced green tea drink with mint against a blurred green field">
    <div class="offer-panel abs"></div>
    <h2 class="offer-title abs" style="font-weight:400">We Offer<br>Premium Quality<br>Herbal Tea</h2>
    <a class="btn btn-shop"><span class="cart-box"><svg viewBox="0 0 10 10"><path d="M1 2h1.5l1.2 4.5h4.3L9 3H3" fill="none" stroke="#fff" stroke-width="1.1"/><circle cx="4" cy="8.3" r=".9" fill="#fff"/><circle cx="7.4" cy="8.3" r=".9" fill="#fff"/></svg></span>SHOP NOW</a>
  </section>

  <section class="newsletter abs">
    <p class="newsletter-text abs">@&nbsp; Get 15 % off teas with e-mail sign-up!</p>
    <a class="btn btn-subscribe">SUBSCRIBE</a>
  </section>

  <div class="field-left abs" role="img" aria-label="Rolling rows of a tea plantation"></div>
  <div class="field-right abs" role="img" aria-label="Rolling rows of a tea plantation"></div>

  <footer class="site-footer abs">
    <div class="footer-col" style="left:30px">
      <h4>Information</h4>
      <ul><li>About Us</li><li>Our Products</li><li>Customer Service</li><li>Terms &amp; Conditions</li><li>Privacy Policy</li><li>Site Map</li><li>FAQ</li><li>Contact Us</li></ul>
    </div>
    <div class="footer-col" style="left:148px">
      <h4>My Account</h4>
      <ul style="line-height:11.4px"><li>Sign In</li><li>View Cart</li><li>My Wishlist</li><li>Track My Order</li><li>Orders &amp; Returns</li><li>Help</li></ul>
    </div>
    <div class="footer-col" style="left:260px">
      <h4>Tea Talk Blog</h4>
      <div class="blog-photo" role="img" aria-label="Seedling sprouting from a white surface"></div>
      <p class="blog-text">Stay Healthy This Spring! Ayurveda is all about balance - how to... <span>Read More »</span></p>
    </div>
    <div class="footer-col" style="left:364px;width:100px">
      <h4 style="margin-left:22px;margin-bottom:6px">Follow us</h4>
      <div class="social" style="margin-left:6px"><span>Socia</span><span>Twine</span><span>Glint</span></div>
      <h4 style="margin:16px 0 4px 16px">Contacts</h4>
      <div class="contact-line"><svg viewBox="0 0 10 10"><path d="M5 1a3 3 0 0 1 3 3c0 2-3 5-3 5S2 6 2 4a3 3 0 0 1 3-3z" fill="var(--green)"/></svg><span>My Company , 12 Fernhill Lane, Glasgow G04 7TW</span></div>
      <div class="contact-line"><svg viewBox="0 0 10 10"><path d="M2 1l2 .5.5 2-1 1a5 5 0 0 0 2 2l1-1 2 .5.5 2-1 1C4 9 1 6 1 2z" fill="var(--green)"/></svg><span>+ 1(800)555-0142</span></div>
    </div>
  </footer>

</div>
</body>
</html>
```